Consultancy Business Card Design

We need a business card design for a new company based in singapore called FortyOne. FortyOne a boutique consultancy firm offering broad-based business solutions, from conception to re-invention, for ventures from new start-ups to long-running traditional businesses.
Its 2 main divisions (Food & Beverage Operations and Construction & Project Management) have access to a wide range of networks, knowledge bases, and resources to service its clients across numerous diverse sectors. This includes, and is not limited to, construction, F&B, and retail.
We are a company that combines the ambition, boldness and energy of one in the 20s with the dedication, level-headedness and dependability of one entering its 30s. Bridging the experiences of the old with ideals of the young, we draw on the positives of both to create a unique synergy.
We hope to see designs that fits our company profile.
Boutique
Contact Information for Business Card
FortyOne(Company Name)
Marcus Tan (Name)
Principle Consultant (Title)
F&B and Hospitality (Division)
(+65) 8364 5107 (Contact no.)
marcus@fortyone-example.com.sg (Email)
Colors
Designer to choose colors to be used in the design.

```html
<!DOCTYPE html>
<html lang="en">
<head>
<meta charset="utf-8">
<title>FortyOne Consultancy – Business Card</title>
<link rel="stylesheet" href="https://fonts.googleapis.com/css2?family=Arimo:wght@400;700&display=swap">
<style>
  :root {
    --page: #ffffff;
    --card-cream: #fffdf0;
    --card-yellow: #fff6c2;
    --wash-yellow: #fde7a6;
    --wash-peach: #f9c39a;
    --wash-pink: #f7b3b3;
    --ink: #111111;
    --band: #b30000;
    --name: #ffffff;
    --edge: #8a8a80;
  }
  * { box-sizing: border-box; margin: 0; padding: 0; }
  html, body { width: 1200px; height: 1000px; overflow: hidden; background: var(--page); }
  body { font-family: "Arimo", Arial, sans-serif; color: var(--ink); position: relative; }

  .card {
    position: absolute;
    width: 600px;
    height: 343px;
    background: linear-gradient(100deg, var(--card-cream) 0%, var(--card-yellow) 100%);
    border: 1px solid var(--edge);
    box-shadow: 2px 3px 6px rgba(0,0,0,0.25);
    overflow: hidden;
  }
  .card--front { left: 120px; top: 140px; }
  .card--back  { left: 480px; top: 520px; }

  .card__wash {
    position: absolute;
    left: 70px; top: 40px; width: 480px; height: 270px;
    border-radius: 50%;
    background: linear-gradient(90deg, var(--wash-yellow) 0%, var(--wash-peach) 60%, var(--wash-pink) 100%);
    opacity: 0.85;
  }

  /* Front */
  .company {
    position: absolute; left: 0; right: 0; top: 62px;
    text-align: center;
    font-size: 44px; font-weight: 700; color: var(--ink);
  }

  .band {
    position: absolute; left: 0; right: 0; top: 168px; height: 44px;
    background: var(--band);
  }
  .band__name {
    position: absolute; left: 0; right: 0; top: 7px;
    text-align: center; font-size: 28px; font-weight: 700; color: var(--name);
  }
  .title {
    position: absolute; left: 0; right: 0; top: 220px;
    text-align: center; font-size: 17px; letter-spacing: 2px;
  }
  .details {
    position: absolute; left: 0; right: 0; top: 262px;
    text-align: center; font-size: 20px; line-height: 30px;
  }

  /* Back */
  .about {
    position: absolute; left: 60px; top: 92px; width: 490px;
    display: grid; grid-template-columns: auto 1fr; column-gap: 8px;
    font-size: 19px; line-height: 21px;
  }
  .label { font-weight: 700; }
  .email {
    position: absolute; left: 110px; top: 245px;
    font-size: 19px;
  }
</style>
</head>
<body>

  <section class="card card--front" aria-label="Business card front">
    <div class="card__wash" aria-hidden="true"></div>
    <p class="company">FortyOne Consultancy</p>
    <div class="band"><div class="band__name">Marcus Tan</div></div>
    <p class="title">Principle Consultant</p>
    <p class="details">Phone: (+65) 8364 5107<br>Division: F&amp;B and Hospitality</p>
  </section>

  <section class="card card--back" aria-label="Business card back">
    <div class="card__wash" aria-hidden="true"></div>
    <div class="about">
      <span class="label">About us:</span>
      <span>FortyOne a boutique consultancy firm offering broad-based business solutions, from conception to re-invention, for ventures from new start-ups to long-running traditional businesses.</span>
    </div>
    <p class="email"><span class="label">eMail:</span> marcus@fortyone-example.com.sg</p>
  </section>

</body>
</html>
```